Premium Website Design for Wellness Practice Consulting Brand

I need a professional website design for my business, The Lanternfield Group.

Please see attached document for homepage formula instructions.

PLEASE NOTE THAT WE ARE NOT A CLINIC.

We are a consulting/strategy brand that helps established wellness practices grow by identifying what is holding them back in their marketing, website, positioning, and patient acquisition.

Our audience includes chiropractors, naturopaths, functional medicine clinics, acupuncturists, physical therapists, and other integrative or holistic practices.

The website needs to feel approachable premium.

It should feel polished, modern, trustworthy, and high-value, but not cold, stiff, or overly corporate.

At the same time, it must avoid looking like a clinic website.

We do not want stock medical visuals, treatment-room aesthetics, or anything that makes people think we provide patient care directly.

The brand should communicate:
- professional
- strategic
- trustworthy
- premium
- clear
- modern
- human
- relevant to wellness practice owners

The design should position us more like a consultant/strategist than a generic marketing agency.

Our main offer is not a long list of services.

Our core offer is helping practice owners see the “holes in the bucket” in their business and marketing, then giving them clarity on what needs to be fixed first.

So the design should support outcome-focused messaging, not “we do websites, SEO, ads, etc.”

Visual direction
I want inspiration from premium brands in the wellness business consulting space, especially the kind of direction seen on The Brightmoor Healer site: confident, elevated, human, and proof-driven, with images of people, leadership, clients, team interaction, wins, and transformation rather than clinical treatment imagery.

Their site emphasizes practitioner growth, leadership, systems, and measurable wins, which is closer to the feeling I want than a traditional clinic or agency site.

Important design goals
- Must clearly look like a business/consulting brand for wellness practices
- Must not be mistaken for a chiropractic, medical, or eye clinic website
- Must not feel tacky, cheap, or “internet marketer”
- Must not feel too sterile or disconnected from the wellness market
- Should feel credible enough for conferences, high-level partnerships, and premium service positioning
- Should feel welcoming enough that smaller or growing practices still feel comfortable reaching out

What I’m looking for
- Strong hierarchy and modern layout
- Clean typography
- Premium but warm color direction
- Smart use of whitespace
- A design that can support testimonials, case studies, authority, and clear calls to action
- A designer who understands brand positioning, not just decoration

Style notes
- Open to pairing DM Sans for body text with a more premium headline font
- Open to colors beyond the current brand mockups, as long as the final direction feels refined and high-trust
- Prefer real human/business-oriented imagery over clinic treatment imagery
- Minimal, elegant, strategic, and conversion-aware is better than flashy or over-designed

EXAMPLE WEBSITES:
This brand has similar target market as we do:
- https://thebrightmoorhealer.example

***The following Websites have a layout we like in terms of following a similar formula:
- https://harlowvalechiropractic.example
- https://brennochiropractic.example
- https://harlowvalemassagetherapy.example
- https://tollerbyphysiorehab.example
- https://orvidex.example

Target Market(s)

chiropractors, naturopaths, functional medicine clinics, acupuncturists, physical therapists, and other integrative or holistic practices.

Industry/Entity Type

Marketing / Consulting

Coding

Font styles to use
Sans Serif

Colors
0054AA
0677BA
7BADD7
CADEEF
E8F1F8

Requirements
Must have
• Home Page / About / Contact / Blog / Services / Testimonials

```html
<!DOCTYPE html>
<html lang="en">
<head>
<meta charset="utf-8">
<title>The Lanternfield Group — Scale Your Wellness Practice</title>
<link href="https://fonts.googleapis.com/css2?family=DM+Sans:wght@400;500;600;700&family=Libre+Baskerville:wght@400;700&display=swap" rel="stylesheet">
<style>
:root{
  --blue:#0054AA;
  --blue-deep:#0A46A0;
  --blue-mid:#0677BA;
  --blue-soft:#7BADD7;
  --blue-pale:#CADEEF;
  --blue-wash:#E3EDF7;
  --ink:#1D1D1F;
  --text:#2E2E33;
  --white:#FFFFFF;
  --serif:'Libre Baskerville', Georgia, serif;
  --sans:'DM Sans', Arial, sans-serif;
}
*{box-sizing:border-box;margin:0;padding:0}
html,body{width:1200px;height:5063px;overflow:hidden}
body{font-family:var(--sans);color:var(--text);background:var(--white);position:relative}
section,header,footer{position:relative;width:1200px}
.abs{position:absolute}
.nowrap{white-space:nowrap}
.btn{position:absolute;display:inline-flex;align-items:center;justify-content:center;height:42px;padding:0 28px;border-radius:21px;font:700 14px var(--sans);text-decoration:none;white-space:nowrap}
.btn-solid{background:var(--blue-deep);color:var(--white)}
.btn-outline{border:2px solid var(--blue-deep);color:var(--blue-deep);background:transparent}
.btn-ghost{border:2px solid var(--white);color:var(--white)}
.h-serif{font-family:var(--serif);font-weight:700;text-transform:uppercase;color:var(--ink);letter-spacing:0}
.eyebrow{font:500 19px var(--sans);color:var(--blue);text-transform:uppercase}
.body-copy{font:400 16px/26px var(--sans);color:var(--text)}

/* header */
.site-header{height:71px;background:var(--white)}
.brand{left:104px;top:20px;font:700 16px/20px var(--serif);color:var(--ink);text-transform:uppercase;letter-spacing:.3px;white-space:nowrap}
.brand small{display:block;font:400 7px var(--serif);letter-spacing:1.5px;margin-top:2px}
.nav{right:104px;top:38px;display:flex;gap:31px}
.nav a{position:relative;font:400 11px var(--serif);color:var(--ink);text-decoration:none;text-transform:uppercase;letter-spacing:.3px}
.nav a.is-active::after{content:"";position:absolute;left:-4px;right:-4px;top:26px;height:2px;background:var(--blue)}

/* hero */
.hero{height:615px;overflow:hidden}
.hero-photo{inset:0;background:linear-gradient(90deg,#E9E9EA 0%,#DCDADA 38%,#B9ABA1 60%,#8A7F78 80%,#5C5F66 100%)}
.hero-title{left:108px;top:96px;font-size:27px;line-height:38px;white-space:nowrap}
.hero-list{left:108px;top:230px;width:480px;list-style:none}
.hero-list li{position:relative;padding-left:28px;font:400 15px/25px var(--sans);color:var(--text);margin-bottom:26px}
.hero-list li::before{content:"";position:absolute;left:0;top:9px;width:7px;height:7px;border-radius:50%;background:var(--blue-deep)}
.scroll-line{left:1116px;top:258px;width:1px;height:230px;background:rgba(255,255,255,.8)}
.scroll-text{top:495px;transform:rotate(90deg);transform-origin:left top;left:1126px;color:var(--white);font:400 16px var(--sans)}
.social{left:1160px;width:12px;height:12px;border-radius:50%;background:var(--white)}

/* approach */
.approach{height:634px}
.rule-label{display:flex;align-items:center;gap:12px}
.rule-label::after{content:"";flex:1;height:1px;background:#C9CCD3}
.approach .eyebrow{left:102px;top:66px;width:488px}
.approach-title{left:102px;top:113px;font-size:24px;line-height:38px;white-space:nowrap}
.frame{border:1.5px solid var(--blue-deep)}
.photo-shadow{box-shadow:0 8px 24px rgba(0,40,100,.18)}

/* steps */
.steps{height:922px;background:var(--blue-wash)}
.center-title{width:1200px;text-align:center}
.steps-label{top:48px;font:500 20px var(--sans);color:var(--blue)}
.steps-title{top:90px;font-size:25px}
.step-line{left:599px;top:143px;width:2px;height:625px;background:var(--blue-deep)}
.pointer{width:0;height:0;border-top:7px solid transparent;border-bottom:7px solid transparent}
.pointer-r{border-left:10px solid var(--blue-deep)}
.pointer-l{border-right:10px solid var(--blue-deep)}
.numeral{font:700 84px/1 var(--sans);letter-spacing:-2px;background:linear-gradient(180deg,var(--blue-deep) 0%,var(--blue-mid) 45%,rgba(123,173,215,0) 100%);-webkit-background-clip:text;background-clip:text;color:transparent}
.step-tag{font:700 15px var(--sans);color:var(--blue-deep)}
.step-head{font:600 28px/34px var(--sans);color:var(--ink);white-space:nowrap}
.step-copy{font:400 13px/21px var(--sans);color:var(--text)}
.right-side{text-align:right}

/* experiences */
.experiences{height:802px}
.exp-label{top:68px;font:500 20px var(--sans);color:var(--blue);text-transform:uppercase}
.exp-title{top:108px;font-size:25px}
.card{top:174px;width:316px;height:517px;background:var(--blue-wash)}
.card.feature{background:var(--white);box-shadow:0 4px 18px rgba(0,40,100,.14)}
.card-photo{left:0;top:0;width:316px;height:249px}
.card-title{left:24px;top:280px;width:280px;font:600 28px/34px var(--sans);color:var(--blue-deep);white-space:nowrap}
.card-copy{left:24px;top:352px;width:270px;font:400 13px/21px var(--sans);color:var(--text)}
.card .btn{left:22px;top:452px}

/* practitioner */
.practitioner{height:619px;background:var(--blue-deep)}
.practitioner .eyebrow{left:106px;top:82px;width:456px;color:var(--white)}
.practitioner .rule-label::after{background:rgba(255,255,255,.4)}
.prac-title{left:104px;top:126px;font-size:25px;color:var(--white)}
.practitioner .body-copy{color:var(--white)}
.frame-light{border:1.5px solid rgba(255,255,255,.6)}

/* testimonials */
.testimonials{height:538px;overflow:hidden}
.t-label{top:54px;font:500 20px var(--sans);color:var(--blue)}
.t-title{top:96px;font-size:24px}
.avatar{border-radius:50%;background:linear-gradient(160deg,#C9B4A4,#6D5A52);border:3px solid var(--white);box-shadow:0 2px 8px rgba(0,0,0,.15)}
.quote{font:400 16px/26px var(--sans);text-align:center;width:540px}
.quote-main{left:330px;top:262px;color:var(--ink)}
.quote-side{top:262px;color:#9A9BA2}
.arrow{top:404px}

/* contact */
.contact{height:564px;background:var(--blue-wash)}
.contact-photo{left:0;top:0;width:560px;height:564px;background:linear-gradient(120deg,#5F5A52 0%,#9C8B78 35%,#C8BBA6 60%,#6E6A66 100%)}
.contact-title{left:613px;top:88px;font-size:24px;white-space:nowrap}
.contact-intro{left:613px;top:128px;width:490px}
.field-label{font:400 16px var(--sans);color:var(--ink)}
.field-line{height:1.5px;background:var(--blue-mid)}

/* footer */
.site-footer{height:298px;background:var(--blue-deep);color:var(--white)}
.foot-brand{top:56px;width:1200px;text-align:center;font:400 40px/1 var(--serif);text-transform:uppercase;letter-spacing:2px;color:var(--white)}
.foot-tag{top:118px;width:1200px;text-align:center;font:400 14px var(--serif);letter-spacing:4px;text-transform:uppercase}
.foot-nav{top:198px;width:1200px;display:flex;justify-content:center;gap:30px}
.foot-nav a{font:700 11px var(--serif);color:var(--white);text-decoration:none;text-transform:uppercase}
.copyright{top:246px;width:1200px;text-align:center;font:400 12px var(--sans)}
</style>
</head>
<body>

<header class="site-header">
  <div class="abs brand">The Lanternfield Group<small>Scale your wellness practice</small></div>
  <nav class="abs nav">
    <a href="#" class="is-active">Home</a><a href="#">About</a><a href="#">Services</a><a href="#">Blog</a><a href="#">Testimonials</a><a href="#">Contact</a>
  </nav>
</header>

<section class="hero">
  <div class="abs hero-photo" role="img" aria-label="Consultant meeting with a smiling practice owner across a table"></div>
  <h1 class="abs h-serif hero-title">Your practice doesn’t need<br>more marketing. It needs<br>clarity.</h1>
  <ul class="abs hero-list">
    <li>Most wellness practices aren’t struggling because they lack effort or skill.</li>
    <li>They’re struggling because something in their business model, messaging, or patient journey is leaking growth.</li>
    <li>We help you find those leaks — and fix them.</li>
  </ul>
  <a class="btn btn-solid" href="#" style="left:108px;top:512px;padding:0 22px">Book a Strategy Call</a>
  <a class="btn btn-outline" href="#" style="left:316px;top:512px;padding:0 30px;background:rgba(255,255,255,.5)">See How We Work</a>
  <span class="abs social" style="top:141px"></span>
  <span class="abs social" style="top:177px"></span>
  <div class="abs scroll-line"></div>
  <div class="abs scroll-text">Scroll</div>
</section>

<section class="approach">
  <div class="abs eyebrow rule-label">Our Approach</div>
  <h2 class="abs h-serif approach-title">Most business coaching<br>teaches strategy and hopes<br>your nervous system keeps up.</h2>
  <p class="abs body-copy" style="left:107px;top:250px;width:480px">Lorem ipsum dolor sit amet, consectetur adipiscing elit, sed do eiusmod tempor incididunt ut labore et dolore magna aliqua. Ut enim ad minim veniam, quis nostrud exercitation ullamco laboris nisi ut aliquip ex ea commodo consequat.</p>
  <p class="abs body-copy" style="left:107px;top:403px;width:480px">Duis aute irure dolor in reprehenderit in voluptate velit esse cillum dolore eu fugiat nulla pariatur. Excepteur sint occaecat cupidatat non proident, sunt in culpa qui officia deserunt mollit anim id est laborum.</p>
  <a class="btn btn-solid" href="#" style="left:108px;top:529px">Learn More</a>
  <div class="abs frame" style="left:648px;top:64px;width:426px;height:419px"></div>
  <div class="abs photo-shadow" role="img" aria-label="Two colleagues reviewing plans at a café table" style="left:674px;top:90px;width:422px;height:418px;background:linear-gradient(135deg,#3A3634 0%,#8C7A68 40%,#C7955A 65%,#D8D2CA 100%)"></div>
</section>

<section class="steps">
  <div class="abs center-title steps-label">Steps</div>
  <h2 class="abs center-title h-serif steps-title">How It Works</h2>
  <div class="abs step-line"></div>

  <div class="abs numeral" style="left:492px;top:155px">01</div>
  <span class="abs pointer pointer-r" style="left:601px;top:157px"></span>
  <div class="abs step-tag" style="left:624px;top:155px">Step 01</div>
  <div class="abs step-head" style="left:626px;top:180px">We Look at What’s<br>Actually Happening</div>
  <p class="abs step-copy" style="left:628px;top:252px;width:390px">Lorem ipsum dolor sit amet, consectetur adipiscing elit, sed do eiusmod tempor incididunt ut labore et dolore magna aliqua. Quis ipsum suspendisse ultrices gravida.</p>

  <span class="abs pointer pointer-l" style="left:589px;top:371px"></span>
  <div class="abs step-tag right-side" style="left:380px;top:369px;width:196px">Step 02</div>
  <div class="abs step-head right-side" style="left:178px;top:394px;width:400px">We Build the Systems<br>That Create Freedom</div>
  <p class="abs step-copy right-side" style="left:190px;top:466px;width:384px">Lorem ipsum dolor sit amet, consectetur adipiscing elit, sed do eiusmod tempor incididunt ut labore et dolore magna aliqua. Quis ipsum suspendisse ultrices gravida. Risus commodo viverra maecenas</p>
  <div class="abs numeral" style="left:622px;top:372px">02</div>

  <div class="abs numeral" style="left:476px;top:588px">03</div>
  <span class="abs pointer pointer-r" style="left:601px;top:577px"></span>
  <div class="abs step-tag" style="left:624px;top:577px">Step 03</div>
  <div class="abs step-head" style="left:626px;top:602px">You Get Real Support</div>
  <p class="abs step-copy" style="left:628px;top:640px;width:390px">Lorem ipsum dolor sit amet, consectetur adipiscing elit, sed do eiusmod tempor incididunt ut labore et dolore magna aliqua. Quis ipsum suspendisse ultrices gravida. Risus commodo viverra maecenas.</p>

  <a class="btn btn-solid" href="#" style="left:529px;top:770px;width:142px;padding:0">Learn More</a>
</section>

<section class="experiences">
  <div class="abs center-title exp-label">Our Core Experiences</div>
  <h2 class="abs center-title h-serif exp-title">Your Next Evolution</h2>

  <article class="abs card" style="left:102px">
    <div class="abs card-photo" role="img" aria-label="Team of professionals collaborating around laptops in an office" style="background:linear-gradient(135deg,#6E6A64,#B9A896 50%,#D9D6D0)"></div>
    <h3 class="abs card-title">Finibus Bonorum<br>et Malorum</h3>
    <p class="abs card-copy">Lorem ipsum dolor sit amet, consectetur adipiscing elit, sed do eiusmod tempor incididunt ut labore et dolore magna aliqua.</p>
    <a class="btn btn-solid" href="#">Learn More</a>
  </article>

  <article class="abs card feature" style="left:442px">
    <div class="abs card-photo" role="img" aria-label="Smiling business advisor in a meeting at a laptop" style="background:linear-gradient(135deg,#D8D6D2,#5B5C5E 50%,#8FA07C)"></div>
    <h3 class="abs card-title">Finibus Bonorum<br>et Malorum</h3>
    <p class="abs card-copy">Quis ipsum suspendisse ultrices gravida. Risus commodo viverra maecenas.</p>
    <a class="btn btn-solid" href="#">Learn More</a>
  </article>

  <article class="abs card" style="left:782px">
    <div class="abs card-photo" role="img" aria-label="Confident practice owner standing with arms crossed" style="background:linear-gradient(135deg,#E6E4E0,#7D7A5E 55%,#D8D4CC)"></div>
    <h3 class="abs card-title">Finibus Bonorum<br>et Malorum</h3>
    <p class="abs card-copy">Lorem ipsum dolor sit amet, consectetur adipiscing elit, sed do eiusmod tempor incididunt ut labore et dolore magna aliqua.</p>
    <a class="btn btn-solid" href="#">Learn More</a>
  </article>
</section>

<section class="practitioner">
  <div class="abs eyebrow rule-label">About Us</div>
  <h2 class="abs h-serif prac-title">Meet Our Practitioner</h2>
  <p class="abs body-copy" style="left:104px;top:179px;width:470px">Lorem ipsum dolor sit amet, consectetur adipiscing elit, sed do eiusmod tempor incididunt ut labore et dolore magna aliqua. Ut enim ad minim veniam, quis nostrud exercitation ullamco laboris nisi ut aliquip ex ea commodo consequat.</p>
  <p class="abs body-copy" style="left:104px;top:332px;width:470px">Duis aute irure dolor in reprehenderit in voluptate velit esse cillum dolore eu fugiat nulla pariatur. Excepteur sint occaecat cupidatat non proident, sunt in culpa qui officia deserunt mollit anim id est laborum.</p>
  <a class="btn btn-ghost" href="#" style="left:103px;top:454px">Learn More</a>
  <div class="abs frame-light" style="left:646px;top:63px;width:426px;height:420px"></div>
  <div class="abs photo-shadow" role="img" aria-label="Practice consultant in a white blazer explaining a strategy" style="left:674px;top:91px;width:422px;height:416px;background:linear-gradient(135deg,#2F3A2C 0%,#7E8C6A 30%,#E8E4DE 60%,#BFB8AE 100%)"></div>
</section>

<section class="testimonials">
  <div class="abs center-title t-label">Testimonials</div>
  <h2 class="abs center-title h-serif t-title">What Our Customer Says</h2>
  <div class="abs avatar" role="img" aria-label="Client portrait" style="left:377px;top:166px;width:75px;height:75px"></div>
  <div class="abs avatar" role="img" aria-label="Client portrait" style="left:463px;top:166px;width:75px;height:75px"></div>
  <div class="abs avatar" role="img" aria-label="Client portrait" style="left:551px;top:154px;width:99px;height:99px"></div>
  <div class="abs avatar" role="img" aria-label="Client portrait" style="left:662px;top:166px;width:75px;height:75px"></div>
  <div class="abs avatar" role="img" aria-label="Client portrait" style="left:747px;top:166px;width:75px;height:75px"></div>
  <p class="abs quote quote-side" style="left:-292px">“Lorem ipsum dolor sit amet, consectetur adipiscing elit, sed do eiusmod tempor incididunt ut labore et dolore magna aliqua. Quis ipsum suspendisse ultrices gravida. Risus commodo viverra maecenas accumsan lacus vel facilisis.”</p>
  <p class="abs quote quote-main">“Lorem ipsum dolor sit amet, consectetur adipiscing elit, sed do eiusmod tempor incididunt ut labore et dolore magna aliqua. Quis ipsum suspendisse ultrices gravida. Risus commodo viverra maecenas accumsan lacus vel facilisis.”</p>
  <p class="abs quote quote-side" style="left:928px">“Lorem ipsum dolor sit amet, consectetur adipiscing elit, sed do eiusmod tempor incididunt ut labore et dolore magna aliqua. Quis ipsum suspendisse ultrices gravida. Risus commodo viverra maecenas accumsan lacus vel facilisis.”</p>
  <svg class="abs arrow" style="left:580px" width="14" height="16" viewBox="0 0 14 16"><path d="M9 2 L3 8 L9 14" fill="none" stroke="#1D1D1F" stroke-width="2"/></svg>
  <svg class="abs arrow" style="left:606px" width="14" height="16" viewBox="0 0 14 16"><path d="M5 2 L11 8 L5 14" fill="none" stroke="#1D1D1F" stroke-width="2"/></svg>
</section>

<section class="contact">
  <div class="abs contact-photo" role="img" aria-label="Thoughtful business owner listening in a bright office"></div>
  <h2 class="abs h-serif contact-title">Let’s Talk About What’s Next</h2>
  <p class="abs body-copy contact-intro">Lorem ipsum dolor sit amet, consectetur adipiscing elit, sed do eiusmod tempor incididunt ut labore et</p>
  <div class="abs field-label" style="left:613px;top:226px">Name</div>
  <div class="abs field-line" style="left:613px;top:261px;width:230px"></div>
  <div class="abs field-label" style="left:865px;top:226px">Email</div>
  <div class="abs field-line" style="left:865px;top:261px;width:233px"></div>
  <div class="abs field-label" style="left:613px;top:308px">Message</div>
  <div class="abs field-line" style="left:613px;top:344px;width:485px"></div>
  <a class="btn btn-solid" href="#" style="left:609px;top:391px;width:142px;padding:0">Submit</a>
</section>

<footer class="site-footer">
  <div class="abs foot-brand">The Lanternfield Group</div>
  <div class="abs foot-tag">Scale your wellness practice</div>
  <nav class="abs foot-nav">
    <a href="#">Home</a><a href="#">About</a><a href="#">Services</a><a href="#">Blog</a><a href="#">Testimonials</a><a href="#">Contact</a>
  </nav>
  <div class="abs copyright">© 2026 | WWW.THELANTERNFIELDGROUP.EXAMPLE</div>
</footer>

</body>
</html>
```